Kelvaro Wp design

We need a wordpress design that will incorporate a professional color scheme with company logo in a clean layout. The design needs to consider that this will be developed on a responsive theme. Colors are undetermined - can use different blue or red as highlight - creative use of colors will be important. Client wants a 'modern' look.

Industry/Entity Type

It Company

Font styles to use
Serif
Sans Serif

Colors

Designer to choose colors to be used in the design.

Requirements
Must have
• - Navigation: 1) Home 2) Real Estate For Sale 3) Auctions 4) About Us 5) Selling Your Property 6) Contact Us

Site will have slideshow - 1st image is attached.
Home Page Content:
My service, experience and dedication provide motivated Sellers and Buyers with a clear marketing advantage. I know that the only way to succeed in real estate is to provide more service than you can get anywhere else. And you will get that kind of service when you work with me.
I will provide you with the personal service you deserve. Put my professional image, reputation, and business ethics to work for you.

Header will have - Logo (attached) Contact Information. 2 Real Estate listing buttons on the right for "New Listings" and "Upcoming Auctions" - similar to http://www.plumtidehomes.example/home

and will have 4 call to action boxes- 1) Land 2) Residential 3) Commercial 4) Auctions

Footer will have site nav, smaller logo, and association logos (attached)
Nice to have
• use of dropdown menus

```html
<!DOCTYPE html>
<html lang="en">
<head>
<meta charset="utf-8">
<title>Kelvaro Realty</title>
<link rel="stylesheet" href="https://fonts.googleapis.com/css2?family=Arimo:wght@400;700&family=Source+Sans+3:wght@400;700&family=Tinos:wght@400;700&display=swap">
<style>
:root{
  --header-grey:#e4e4e4;
  --brand-red:#cc0b12;
  --nav-divider:#a8070d;
  --navy:#383a66;
  --navy-dark:#22234a;
  --button-navy:#3c3f6e;
  --white:#ffffff;
  --text-light:#f1f1f6;
}
*{margin:0;padding:0;box-sizing:border-box}
html,body{width:1196px;height:1200px;overflow:hidden}
body{position:relative;background:var(--navy);font-family:"Source Sans 3",sans-serif;color:var(--text-light)}
.site-header{position:absolute;left:0;top:0;width:1196px;height:143px;background:var(--header-grey)}
.brand{position:absolute;left:112px;top:40px;display:flex;align-items:center;gap:10px;font-family:"Arimo",sans-serif;font-weight:700;font-size:30px;letter-spacing:1px;color:var(--navy-dark)}
.brand-dot{width:22px;height:22px;border-radius:50%;background:var(--navy-dark)}
.listing-button{position:absolute;height:46px;border-radius:8px;background:var(--button-navy);color:var(--white);font-family:"Tinos",serif;font-size:21px;display:flex;align-items:center;box-shadow:2px 3px 3px rgba(0,0,0,.3)}
.listing-button svg{position:absolute}
.new-listings{left:600px;top:60px;width:187px;padding-left:47px}
.new-listings svg{left:-48px;top:-8px}
.upcoming-auctions{left:840px;top:58px;width:243px;padding-left:57px}
.upcoming-auctions svg{left:-10px;top:-4px}
.main-nav{position:absolute;left:0;top:145px;width:1196px;height:44px;background:var(--brand-red)}
.nav-item{position:absolute;top:0;height:44px;line-height:42px;font-family:"Arimo",sans-serif;font-size:16px;color:var(--white);transform:translateX(-50%);white-space:nowrap}
.nav-divider{position:absolute;top:7px;width:1px;height:32px;background:var(--nav-divider)}
.dropdown{position:absolute;left:451px;top:189px;width:157px;height:86px;background:var(--navy-dark);padding:6px 6px;font-family:"Arimo",sans-serif;font-size:14px}
.dropdown div{height:31px;line-height:32px;padding-left:12px;color:var(--white)}
.dropdown .active{background:var(--brand-red)}
.hero{position:absolute;left:110px;top:206px;width:976px;height:379px;border:4px solid var(--white);background:linear-gradient(180deg,#b9c7a4 0%,#6f7a52 40%,#7c5a45 58%,#4f7a2f 70%,#6aa040 100%)}
.intro{position:absolute;left:150px;top:615px;width:884px;text-align:center;font-size:15.5px;line-height:22px;letter-spacing:.2px}
.intro strong{display:block;margin-top:22px;font-weight:700}
.cta{position:absolute;top:779px;width:236px}
.cta-title{height:44px;background:var(--brand-red);border-radius:4px;text-align:center;font-family:"Tinos",serif;font-weight:700;font-size:25px;line-height:44px;color:var(--white);text-shadow:1px 2px 2px rgba(0,0,0,.5)}
.cta-photo{margin-top:10px;height:133px;border:4px solid var(--white)}
.site-footer{position:absolute;left:0;top:1052px;width:1196px;height:148px;background:var(--brand-red);font-family:"Arimo",sans-serif;color:var(--white)}
.footer-nav{position:absolute;left:106px;top:36px;font-size:14px}
.footer-nav span{margin:0 10px}
.copyright{position:absolute;left:104px;top:84px;font-size:14px}
.footer-brand{position:absolute;left:877px;top:22px;display:flex;align-items:center;gap:8px;font-weight:700;font-size:22px;letter-spacing:1px}
.footer-brand .brand-dot{width:16px;height:16px;background:var(--white)}
.badges{position:absolute;left:807px;top:88px;display:flex;gap:18px}
.badges div{background:var(--white);height:46px;border-radius:3px}
</style>
</head>
<body>
<header class="site-header">
  <div class="brand"><span class="brand-dot"></span>KELVARO REALTY</div>
  <div class="listing-button new-listings">
    <svg width="82" height="58" viewBox="0 0 82 58"><polygon points="8,28 40,4 72,28" fill="#8a4a2a"/><rect x="16" y="26" width="48" height="28" fill="#f1e3c8"/><rect x="34" y="36" width="12" height="18" fill="#7a4a2a"/><circle cx="10" cy="14" r="10" fill="#d8131a"/></svg>
    New Listings
  </div>
  <div class="listing-button upcoming-auctions">
    <svg width="54" height="52" viewBox="0 0 54 52"><rect x="2" y="6" width="48" height="44" rx="3" fill="#f3f6fb" stroke="#aab4c8"/><rect x="2" y="6" width="48" height="10" fill="#d8131a"/><g fill="#b8c6dc"><rect x="8" y="22" width="8" height="6"/><rect x="20" y="22" width="8" height="6"/><rect x="32" y="22" width="8" height="6"/><rect x="8" y="32" width="8" height="6"/><rect x="20" y="32" width="8" height="6"/><rect x="32" y="32" width="8" height="6"/></g></svg>
    Upcoming Auctions
  </div>
</header>

<nav class="main-nav">
  <span class="nav-item" style="left:139px">Home</span>
  <span class="nav-divider" style="left:205px"></span>
  <span class="nav-item" style="left:314px">Real Estate For Sale</span>
  <span class="nav-divider" style="left:416px"></span>
  <span class="nav-item" style="left:495px">Auctions</span>
  <span class="nav-divider" style="left:566px"></span>
  <span class="nav-item" style="left:643px">About Us</span>
  <span class="nav-divider" style="left:708px"></span>
  <span class="nav-item" style="left:832px">Selling Your Property</span>
  <span class="nav-divider" style="left:948px"></span>
  <span class="nav-item" style="left:1028px">Contact Us</span>
</nav>

<div class="hero" role="img" aria-label="Slideshow photo of a brick ranch house with a porch among tall trees and a green lawn"></div>

<div class="dropdown">
  <div>Upcoming Auction</div>
  <div class="active">Past Auction</div>
</div>

<section class="intro">
  <p>My service, experience and dedication provide motivated Sellers and Buyers with a clear marketing advantage. I know that the only way to succeed in real estate is to provide more service than you can get anywhere else. And you will get that kind of service when you work with me.</p>
  <strong>I will provide you with the personal service you deserve. Put my professional image, reputation, and business ethics to work for you.</strong>
</section>

<div class="cta" style="left:109px"><div class="cta-title">Land</div><div class="cta-photo" role="img" aria-label="Photo of open farmland with a wooden fence under a blue sky" style="background:linear-gradient(180deg,#b8cde6 0%,#e2e8ef 45%,#5f7a3a 60%,#a8a06a 100%)"></div></div>
<div class="cta" style="left:356px"><div class="cta-title">Residential</div><div class="cta-photo" role="img" aria-label="Photo of a shingled house with a flower garden" style="background:linear-gradient(180deg,#dfe6ea 0%,#8f8a88 40%,#9c7ab0 62%,#4f8f3a 100%)"></div></div>
<div class="cta" style="left:602px"><div class="cta-title">Commercial</div><div class="cta-photo" role="img" aria-label="Photo of a modern glass building lit at night" style="background:linear-gradient(160deg,#0d2a9a 0%,#2a55d8 45%,#c98a3a 65%,#10207a 100%)"></div></div>
<div class="cta" style="left:849px"><div class="cta-title">Auctions</div><div class="cta-photo" role="img" aria-label="Photo of a crowd gathered in front of a house at an auction" style="background:linear-gradient(180deg,#cfd3d6 0%,#8b8e92 45%,#3a3c42 75%,#c8c9cc 100%)"></div></div>

<footer class="site-footer">
  <div class="footer-nav">Home<span>|</span>Real Estate For Sale<span>|</span>Auctions<span>|</span>About Us<span>|</span>Selling Your Property<span>|</span>Contact Us</div>
  <div class="copyright">Copyright © 2014 Kelvaro Realty,LLC . All rights reserved.</div>
  <div class="footer-brand"><span class="brand-dot"></span>KELVARO</div>
  <div class="badges">
    <div style="width:42px"></div>
    <div style="width:90px"></div>
    <div style="width:40px"></div>
    <div style="width:44px"></div>
  </div>
</footer>
</body>
</html>
```